Business Card and Letterhead for new HR Consultancy

A business card and letterhead design that includes the logo (attached in jpg) and the business tag line which is "Investing in Your Greatest Asset"
We are based in regional New South Wales, Australia and provide HR services to small and medium business owners to support them grow their businesses by focusing on their people. The services provided cover the full range of HR management from simple advice through to comprehensive programs that support people management. My clients typically will not have a HR manager, either because they don't need to employ one or can't afford to hire one. So they will be looking for me to provide good services, add value to their business for a competitive price.
I am a middle aged woman with over 15 years expertise in all facets of HR Management. My clients need to know they can trust me, that I am credible and competent and open in my relationship with them and that I can make a positive difference for them.
I would like to see designs that are modern and communicate value for money.
A note to advise that the email address is
xxxxxxx@wattlecrestteam.com.au
website will be
www.wattlecrestteam.com.au
thanks
L.
Will also need to include the business number (indicates it is a registered business).
ABN: 38 217 405 963
Target Market(s)
small to medium sized business owners 30 years and over, professional and tradespeople
Industry/Entity Type
Business
Look and feel

```html
<!DOCTYPE html>
<html lang="en">
<head>
<meta charset="utf-8">
<title>Wattlecrest Stationery</title>
<link href="https://fonts.googleapis.com/css2?family=Open+Sans:wght@300;400;600;700&display=swap" rel="stylesheet">
<style>
  :root {
    --backdrop: #a9a9a9;
    --paper: #ffffff;
    --green: #237629;
    --green-soft: #3f8d45;
    --brown: #6b3522;
    --red: #d7141a;
    --ink: #6e6e6e;
    --ink-dark: #4a4a4a;
    --ghost: #f2f2f2;
  }
  html, body {
    margin: 0;
    padding: 0;
    width: 1200px;
    height: 900px;
    overflow: hidden;
    background: var(--backdrop);
    font-family: "Open Sans", Arial, sans-serif;
  }
  .canvas { position: relative; width: 1200px; height: 900px; }

  /* Shared brand lockup */
  .brand { position: absolute; display: flex; align-items: center; }
  .brand .dot { border-radius: 50%; background: var(--green); flex: none; }
  .brand .wordmark { display: flex; flex-direction: column; align-items: flex-end; }
  .brand .brand-name { color: var(--green); font-weight: 600; letter-spacing: -0.3px; white-space: nowrap; }
  .brand .tagline { color: var(--red); font-weight: 700; white-space: nowrap; text-transform: uppercase; }

  /* Business card front */
  .card { position: absolute; left: 106px; width: 252px; height: 144px; overflow: hidden; }
  .card-front { top: 79px; background: var(--green); }
  .card-front .ghost-mark {
    position: absolute; left: 20px; top: 14px; width: 110px; height: 110px;
    border-radius: 50%; background: var(--green-soft);
  }
  .card-front .wordmark {
    position: absolute; right: 10px; top: 105px;
    display: flex; flex-direction: column; align-items: flex-end;
  }
  .card-front .brand-name {
    color: var(--paper); font-weight: 600; font-size: 19px; line-height: 22px;
    letter-spacing: -0.3px; white-space: nowrap;
  }
  .card-front .tagline {
    color: var(--red); font-weight: 700; font-size: 4.6px; line-height: 6px;
    text-transform: uppercase; white-space: nowrap; margin-top: -2px;
  }

  /* Business card back */
  .card-back { top: 234px; background: var(--paper); }
  .card-back .ghost-mark {
    position: absolute; right: -12px; top: 12px; width: 110px; height: 110px;
    border-radius: 50%; background: var(--ghost);
  }
  .card-back .brand { left: 9px; top: 11px; }
  .card-back .brand .dot { width: 14px; height: 14px; margin-right: 5px; }
  .card-back .brand .brand-name { font-size: 16px; line-height: 18px; }
  .card-back .brand .tagline { font-size: 4.2px; line-height: 5px; margin-top: -1px; }
  .card-back .postal {
    position: absolute; left: 11px; top: 73px;
    font-size: 6px; line-height: 8px; color: var(--ink); font-weight: 300;
  }
  .card-back .person { position: absolute; right: 13px; top: 87px; text-align: right; z-index: 1; }
  .card-back .person-name { font-size: 9.5px; font-weight: 600; color: var(--green); line-height: 11px; }
  .card-back .person-role { font-size: 6px; line-height: 8px; color: var(--ink); font-weight: 300; }
  .card-back .contacts {
    position: absolute; left: 11px; top: 109px; margin: 0; padding: 0; list-style: none;
    font-size: 6px; line-height: 9px; color: var(--ink); font-weight: 300;
  }
  .card-back .contacts li { display: flex; align-items: center; white-space: nowrap; }
  .card-back .contacts svg { width: 6px; height: 6px; margin-right: 4px; fill: var(--green); flex: none; }
  .colour-band { position: absolute; left: 0; bottom: 0; display: flex; width: 100%; }
  .colour-band .band-green { background: var(--green); }
  .colour-band .band-brown { background: var(--brown); flex: 1; }
  .card-back .colour-band { height: 4px; }
  .card-back .band-green { width: 180px; }

  /* Letterhead */
  .letterhead {
    position: absolute; left: 391px; top: 66px; width: 612px; height: 792px;
    background: var(--paper); overflow: hidden;
  }
  .letterhead .ghost-mark {
    position: absolute; left: 410px; top: 490px; width: 300px; height: 300px;
    border-radius: 50%; background: var(--ghost);
  }
  .letterhead .brand { left: 26px; top: 44px; }
  .letterhead .brand .dot { width: 28px; height: 28px; margin-right: 10px; }
  .letterhead .brand .brand-name { font-size: 32px; line-height: 36px; }
  .letterhead .brand .tagline { font-size: 7.4px; line-height: 9px; margin-top: -2px; }
  .letterhead .address {
    position: absolute; left: 502px; top: 47px; font-style: normal;
    font-size: 9.5px; line-height: 12px; color: var(--ink); font-weight: 300;
  }
  .letterhead .address .label { color: var(--green); font-weight: 400; }
  .letterhead .web {
    position: absolute; right: 16px; top: 766px; z-index: 1;
    font-size: 9.5px; line-height: 12px; color: var(--ink-dark);
  }
  .letterhead .colour-band { height: 10px; z-index: 1; }
  .letterhead .band-green { width: 447px; }
</style>
</head>
<body>
<div class="canvas">

  <section class="card card-front" aria-label="Business card front">
    <div class="ghost-mark"></div>
    <div class="wordmark">
      <span class="brand-name">Wattlecrest</span>
      <span class="tagline">Investing in Your Greatest Asset</span>
    </div>
  </section>

  <section class="card card-back" aria-label="Business card back">
    <div class="ghost-mark"></div>
    <div class="brand">
      <span class="dot"></span>
      <span class="wordmark">
        <span class="brand-name">Wattlecrest</span>
        <span class="tagline">Investing in Your Greatest Asset</span>
      </span>
    </div>
    <div class="postal">PO Box 718<br>Orange NSW 2800<br>ABN 38 217 405 963</div>
    <div class="person">
      <div class="person-name">Mara Ellison</div>
      <div class="person-role">Marketing Manager</div>
    </div>
    <ul class="contacts">
      <li><svg viewBox="0 0 10 10"><path d="M1 3c0-1 1-2 4-2s4 1 4 2v1H7V3H3v1H1zM2 5h6l1 4H1z"/></svg>02-6354-1190</li>
      <li><svg viewBox="0 0 10 10"><path d="M0 2h10v6H0zM1 3v.4l4 2.6 4-2.6V3L5 5.3z" fill-rule="evenodd"/></svg>mellison@wattlecrestteam.com.au</li>
      <li><svg viewBox="0 0 10 10"><circle cx="5" cy="5" r="4.5"/></svg>www.wattlecrestteam.com.au</li>
    </ul>
    <div class="colour-band"><span class="band-green"></span><span class="band-brown"></span></div>
  </section>

  <section class="letterhead" aria-label="Letterhead">
    <div class="ghost-mark"></div>
    <div class="brand">
      <span class="dot"></span>
      <span class="wordmark">
        <span class="brand-name">Wattlecrest</span>
        <span class="tagline">Investing in Your Greatest Asset</span>
      </span>
    </div>
    <address class="address">
      418 Kestrel Road<br>
      Orange NSW 2800<br>
      <span class="label">P.</span> (02) 6354 1187<br>
      <span class="label">F.</span> (02) 6354 1187<br>
      ABN 38 217 405 963
    </address>
    <div class="web">www.wattlecrestteam.com.au</div>
    <div class="colour-band"><span class="band-green"></span><span class="band-brown"></span></div>
  </section>

</div>
</body>
</html>
```